Mobile app for deals

Mobile App Name: Tradeyard

Design screen shots for the issue of quotes for deals.

1. Loading screen
2. User signs in with credentials or signs up
2. Search by category
3. Search by location
4. Create a project

The expected experience after a project is placed:
- Project alerted
- Quotes
- Project complete
- Rating
- Payment

#TotallyExcited
Updates

Project Deadline Extended Reason: Deadline has been extended on request from a few designers who saw the project late and who would like to submit designs.Thank you to all who submitted on time, we are reviewing your designs and will respond shortly. Added Monday, June 29, 2015

Target Market(s)

Contractors market

Industry/Entity Type

Business Directory

Font styles to use
Sans Serif

Requirements
Must have
• Simple design
• User friendly
• Translateable (later)

```html
<!DOCTYPE html>
<html lang="en">
<head>
<meta charset="utf-8">
<title>Tradeyard – Welcome</title>
<link href="https://fonts.googleapis.com/css2?family=Lato:wght@400;700;900&display=swap" rel="stylesheet">
<style>
  :root {
    --backdrop: #2c3038;
    --screen: #ffffff;
    --brand-blue: #3a7ab5;
    --brand-dark: #3a3a3c;
    --ink: #1f1f1f;
    --rule: #555555;
    --button-text: #ffffff;
  }
  html, body {
    margin: 0;
    padding: 0;
    width: 1200px;
    height: 1139px;
    overflow: hidden;
    background: var(--backdrop);
    font-family: "Lato", sans-serif;
  }
  .app-screen {
    position: absolute;
    left: 300px;
    top: 36px;
    width: 600px;
    height: 1066px;
    background: var(--screen);
    overflow: hidden;
  }
  .brand {
    position: absolute;
    top: 150px;
    left: 0;
    width: 100%;
    display: flex;
    flex-direction: column;
    align-items: center;
  }
  .brand-mark {
    width: 190px;
    height: 190px;
  }
  .brand-name {
    margin-top: 26px;
    font-size: 58px;
    font-weight: 900;
    color: var(--brand-dark);
    letter-spacing: 0.5px;
  }
  .team-photo {
    position: absolute;
    left: 0;
    top: 470px;
    width: 100%;
    height: 470px;
    background:
      linear-gradient(180deg, rgba(255,255,255,1) 0%, rgba(255,255,255,0.35) 30%, rgba(255,255,255,0.35) 100%),
      linear-gradient(90deg, #c9b8a0 0%, #9aa3ad 25%, #d4cbc2 45%, #c7a6a0 65%, #8fa6c6 85%, #6f8fbf 100%);
  }
  .audience-choice {
    position: absolute;
    top: 560px;
    left: 0;
    width: 100%;
    text-align: center;
    color: var(--ink);
    font-size: 27px;
    line-height: 1.3;
  }
  .audience-choice p { margin: 0; }
  .how-link {
    color: var(--brand-blue);
    text-decoration: none;
    display: inline-block;
  }
  .divider {
    display: flex;
    align-items: center;
    justify-content: center;
    gap: 14px;
    margin: 10px 0 12px;
    font-size: 16px;
    letter-spacing: 1px;
  }
  .divider::before, .divider::after {
    content: "";
    width: 80px;
    height: 1px;
    background: var(--rule);
  }
  .auth-actions {
    position: absolute;
    left: 0;
    bottom: 0;
    width: 100%;
    height: 126px;
    display: flex;
  }
  .auth-button {
    flex: 1;
    display: flex;
    align-items: center;
    justify-content: center;
    color: var(--button-text);
    font-size: 26px;
    font-weight: 700;
    letter-spacing: 1.5px;
    text-decoration: none;
  }
  .auth-button--sign-in { background: var(--brand-dark); }
  .auth-button--register { background: var(--brand-blue); }
</style>
</head>
<body>
  <main class="app-screen">
    <div class="team-photo" role="img" aria-label="Faded photo of a group of tradespeople in work clothes and hard hats"></div>

    <header class="brand">
      <svg class="brand-mark" viewBox="0 0 190 190" aria-hidden="true">
        <circle cx="95" cy="95" r="90" fill="var(--brand-blue)"/>
      </svg>
      <div class="brand-name">Tradeyard</div>
    </header>

    <section class="audience-choice">
      <p>Are you a professional looking for work?</p>
      <a class="how-link" href="#">How it works?</a>
      <div class="divider">OR</div>
      <p>Are you looking for a professional<br>to do work?</p>
      <a class="how-link" href="#">How it works?</a>
    </section>

    <nav class="auth-actions">
      <a class="auth-button auth-button--sign-in" href="#">SIGN IN</a>
      <a class="auth-button auth-button--register" href="#">REGISTER</a>
    </nav>
  </main>
</body>
</html>
```